Layout for new page on existing website

We have an existing website (www.brightmillworks.org) and need a new page designing to promote a new product.
The new page needs to be consistent with the existing website look and feel (www.brightmillworks.org) but current persistent elements on the standard page design can be moved/removed from the page to accommodate a new layout necessary for getting all the content laid out in a logical user friendly way.
The content required for the page is attached along with a wireframe mock up that may help understand the expectation, however the wireframe was just created to help me work out what was needed on the page and the layout can be different. A key element is the quality of the design of each of the artifacts (e.g. the panel the embedded video needs to go in, icons etc) and a clear display of the information.
Updates
The website that the new page needs to fit into is www.brightmillworks.org, i will also added the company logo to the brief.
Our Corporate Colours
- Green: #A2FF00
- Cream: #FFFF99
- Yellow: #FFE900
- Grey: #534741

```html
<!DOCTYPE html>
<html lang="en">
<head>
<meta charset="utf-8">
<title>Brightmill Works – Course Management &amp; Booking</title>
<link href="https://fonts.googleapis.com/css2?family=PT+Sans:ital,wght@0,400;0,700;1,400;1,700&display=swap" rel="stylesheet">
<style>
  :root{
    --page-bg:#4a403a;
    --page-bg-dark:#3e3530;
    --panel-bg:#2e2723;
    --panel-line:#5e544c;
    --cream:#ffff99;
    --yellow:#ffe900;
    --gold:#f3d23a;
    --green:#a2ff00;
    --text:#f2efe9;
    --text-muted:#9c928a;
    --ink:#3b3430;
  }
  *{box-sizing:border-box;margin:0;padding:0}
  html,body{width:1200px;height:2250px;overflow:hidden}
  body{
    background:linear-gradient(90deg,var(--page-bg-dark) 0,var(--page-bg) 60px,var(--page-bg) 1140px,var(--page-bg-dark) 1200px);
    font-family:"PT Sans",Arial,sans-serif;color:var(--text);position:relative;
  }
  .abs{position:absolute}

  /* header */
  .home-link{left:88px;top:104px;width:60px;text-align:center;color:var(--text);font-size:15px;text-decoration:none}
  .home-link svg{display:block;margin:0 auto 8px}
  .brand{left:0;width:1200px;top:86px;text-align:center;font-weight:700;font-size:42px;letter-spacing:9px;color:#fff}
  .brand .dot{display:inline-block;width:34px;height:34px;border-radius:50%;background:var(--green);vertical-align:2px;margin-right:18px}
  .tagline{left:0;width:1200px;top:160px;text-align:center;color:var(--cream);font-size:31px;font-weight:700}

  /* hero */
  .hero{left:75px;top:237px;width:1045px;height:268px;border-radius:8px;overflow:hidden;
    background:linear-gradient(100deg,#c9a37d 0%,#e8c8a4 30%,#8a5a3a 55%,#b98a60 75%,#e3d3c2 100%)}
  .hero-caption{left:0;bottom:0;width:460px;height:118px;padding:22px 28px;
    background:linear-gradient(90deg,rgba(255,255,255,.55),rgba(255,255,255,0));
    color:var(--ink);font-weight:700;font-size:33px;line-height:40px}

  /* video */
  .video{left:75px;top:537px;width:482px;height:318px;background:#fff;border-radius:14px;padding:10px;box-shadow:0 4px 12px rgba(0,0,0,.35)}
  .video-screen{width:462px;height:252px;border-radius:8px 8px 0 0;position:relative;
    background:linear-gradient(160deg,#3d64a8 0%,#dfe8f5 30%,#f4f6fa 100%)}
  .video-screen .play{position:absolute;left:196px;top:96px;width:68px;height:62px;background:rgba(60,60,60,.8);border-radius:6px}
  .video-controls{height:46px;display:flex;align-items:center;gap:14px;padding:0 10px}
  .video-controls .track{flex:1;height:4px;background:#bbb;border-radius:2px}

  /* testimonial */
  .testimonial{left:587px;top:542px;width:520px}
  .testimonial h2{color:var(--cream);font-size:27px;font-weight:700;margin-bottom:20px}
  .testimonial blockquote{font-size:20px;line-height:26px;font-weight:700;color:var(--text)}
  .testimonial .author{margin-top:16px;color:var(--cream);font-style:italic;font-weight:700;font-size:20px;line-height:25px}

  .btn{display:flex;align-items:center;gap:14px;border-radius:10px;
    background:linear-gradient(#fffbb8,#f4e25a 55%,#e8c92a);color:var(--ink);
    box-shadow:0 3px 8px rgba(0,0,0,.45);text-decoration:none}
  .btn-small{left:587px;top:783px;width:376px;height:66px;padding:0 18px}
  .btn-small .lines{line-height:22px}
  .btn-small .sub{font-size:17px}
  .btn-small .main{font-size:24px;font-weight:700}

  /* features */
  .feature{width:480px;display:flex;gap:16px}
  .feature .icon{flex:0 0 68px}
  .feature h3{color:var(--cream);font-style:italic;font-weight:700;font-size:20px;line-height:24px}
  .feature p{font-size:19px;line-height:24px;color:var(--text)}

  /* benefits */
  .benefits{left:75px;top:1392px;width:1045px;height:788px;background:var(--panel-bg);border:2px solid var(--panel-line);border-radius:14px;padding:30px 40px}
  .benefits h2{color:var(--cream);font-style:italic;font-weight:700;font-size:31px;margin-bottom:16px}
  .benefits ul{list-style:none}
  .benefits li{position:relative;padding-left:24px;font-size:19px;line-height:25px;margin-bottom:19px}
  .benefits li::before{content:"";position:absolute;left:0;top:7px;width:11px;height:11px;background:var(--yellow)}
  .btn-large{left:112px;top:2070px;width:975px;height:80px;padding:0 26px;gap:30px}
  .btn-large .main{font-size:26px;font-weight:700;line-height:28px}
  .btn-large .sub{font-size:18px}

  .footer{left:85px;top:2203px;font-size:15px;color:var(--text-muted)}
</style>
</head>
<body>

<a class="abs home-link" href="#">
  <svg width="44" height="40" viewBox="0 0 44 40"><path d="M4 20 22 4 40 20" fill="none" stroke="#f3d23a" stroke-width="4" stroke-linejoin="round"/><path d="M10 18v18h24V18" fill="none" stroke="#f3d23a" stroke-width="4"/><rect x="19" y="25" width="7" height="11" fill="#f3d23a"/></svg>
  Home
</a>
<div class="abs brand"><span class="dot"></span>BRIGHTMILL WORKS</div>
<div class="abs tagline">Cource Management &amp; Booking Simplified</div>

<section class="abs hero" role="img" aria-label="Photo of hands typing on a laptop keyboard in an office">
  <div class="abs hero-caption">Built with only<br>your business in mind</div>
</section>

<div class="abs video">
  <div class="video-screen" role="img" aria-label="Product video preview showing the course booking admin screen">
    <div class="play"><svg width="68" height="62" viewBox="0 0 68 62"><path d="M24 16 48 31 24 46Z" fill="#fff"/></svg></div>
  </div>
  <div class="video-controls">
    <svg width="20" height="22" viewBox="0 0 20 22"><path d="M2 1 19 11 2 21Z" fill="#333"/></svg>
    <div class="track"></div>
    <svg width="22" height="22" viewBox="0 0 22 22"><circle cx="5" cy="11" r="3" fill="#555"/><circle cx="17" cy="4" r="3" fill="#555"/><circle cx="17" cy="18" r="3" fill="#555"/><path d="M5 11 17 4M5 11l12 7" stroke="#555" stroke-width="2"/></svg>
    <svg width="24" height="20" viewBox="0 0 24 20"><rect x="1" y="1" width="22" height="14" fill="none" stroke="#555" stroke-width="2"/><rect x="8" y="16" width="8" height="3" fill="#555"/></svg>
    <svg width="24" height="20" viewBox="0 0 24 20"><path d="M2 7h5l6-5v16l-6-5H2Z" fill="#555"/><path d="M17 5q4 5 0 10" fill="none" stroke="#555" stroke-width="2"/></svg>
  </div>
</div>

<section class="abs testimonial">
  <h2>Happy Customers Says</h2>
  <blockquote>“A convenient tool that was simple to integrate into our website. It has allowed both the business and our customers an easy way to book courses. In life sometimes simple is good and this is a great example!”</blockquote>
  <p class="author">Clara Dunmore, Director @ PeakTutor<br>www.peaktutor.org</p>
</section>

<a class="abs btn btn-small" href="#">
  <svg width="46" height="34" viewBox="0 0 46 34"><path d="M4 12q19-12 38 0l-3 7-8-3v-4q-8-3-16 0v4l-8 3Z" fill="#3b3430"/><rect x="12" y="20" width="22" height="12" rx="3" fill="#3b3430"/></svg>
  <span class="lines"><span class="sub">Discuss about your requiroment</span><br><span class="main">Contact Us Now</span></span>
</a>

<!-- features: left column -->
<div class="abs feature" style="left:78px;top:917px">
  <svg class="icon" width="68" height="68" viewBox="0 0 68 68"><circle cx="34" cy="34" r="30" fill="#f3d23a"/><circle cx="34" cy="34" r="19" fill="none" stroke="#3b3430" stroke-width="5"/><path d="M34 22v13h9" fill="none" stroke="#3b3430" stroke-width="5"/></svg>
  <div><h3>Available and easy to use 24/7</h3><p>By allowing booking and payment at any time of the day, your attendees will be more likely to commit to your event and with no account setup or password required and no paper forms to fill in and post, booking onto and paying for your courses is easy.</p></div>
</div>
<div class="abs feature" style="left:78px;top:1103px">
  <svg class="icon" width="68" height="68" viewBox="0 0 68 68"><circle cx="34" cy="34" r="30" fill="#f3d23a"/><rect x="19" y="21" width="30" height="24" rx="2" fill="none" stroke="#3b3430" stroke-width="4"/><path d="M25 29h18M25 36h18M28 50h12" stroke="#3b3430" stroke-width="4"/></svg>
  <div><h3>Online Course promotion</h3><p>List your upcoming courses in a clear and simple way so people can easily find and select the course that suits them.</p></div>
</div>
<div class="abs feature" style="left:78px;top:1220px">
  <svg class="icon" width="68" height="68" viewBox="0 0 68 68"><circle cx="34" cy="34" r="30" fill="#f3d23a"/><path d="M20 35l10 10 19-21" fill="none" stroke="#3b3430" stroke-width="7" stroke-linecap="round" stroke-linejoin="round"/></svg>
  <div><h3>Live course place availability</h3><p>By defining minimum and maximum candidates permitted on a course its easy to prevent over-booking and also prevent courses running that don’t have enough candidates.</p></div>
</div>

<!-- features: right column -->
<div class="abs feature" style="left:612px;top:917px">
  <svg class="icon" width="68" height="68" viewBox="0 0 68 68"><circle cx="34" cy="34" r="30" fill="#f3d23a"/><path d="M22 46l4-12 18-18 8 8-18 18Z" fill="#3b3430"/></svg>
  <div><h3>Customisable look and feel</h3><p>All elements of the booking systems design will fit in with your existing websites style.</p></div>
</div>
<div class="abs feature" style="left:612px;top:1017px">
  <svg class="icon" width="68" height="68" viewBox="0 0 68 68"><circle cx="34" cy="34" r="30" fill="#f3d23a"/><rect x="18" y="23" width="32" height="22" fill="none" stroke="#3b3430" stroke-width="4"/><path d="M18 23l16 12 16-12" fill="none" stroke="#3b3430" stroke-width="4"/></svg>
  <div><h3>Built in email system</h3><p>Enable quick and easy communication with upcoming course candidates and promotion of additional courses to past candidates.</p></div>
</div>
<div class="abs feature" style="left:612px;top:1145px">
  <svg class="icon" width="68" height="68" viewBox="0 0 68 68"><circle cx="34" cy="34" r="30" fill="#f3d23a"/><circle cx="34" cy="34" r="20" fill="none" stroke="#3b3430" stroke-width="3"/><text x="34" y="44" text-anchor="middle" font-family="PT Sans, sans-serif" font-weight="700" font-size="28" fill="#3b3430">$</text></svg>
  <div><h3>Online &amp; Offline Payments</h3><p>Take payments online, whilst having the flexibility of managing and adding offline payments.</p></div>
</div>
<div class="abs feature" style="left:612px;top:1265px">
  <svg class="icon" width="68" height="68" viewBox="0 0 68 68"><circle cx="34" cy="34" r="30" fill="#f3d23a"/><path d="M34 52c-10-12-14-18-14-24a14 14 0 0 1 28 0c0 6-4 12-14 24Z" fill="#3b3430"/><circle cx="34" cy="28" r="5" fill="#f3d23a"/></svg>
  <div><h3>Venue database management</h3><p>Easily add, edit and remove venues from which you operate your courses from.</p></div>
</div>

<section class="abs benefits">
  <h2>Key Benefits</h2>
  <ul>
    <li>Live Availability - Availability on course place availability to prevent overbooking Customers can search for Courses and Book Online with immediate confirmation Automated confirmation emails</li>
    <li>Be available for business 24/7 and take orders anytime! Customers can book when it’s most convenient for them - be it early morning, late evening or weekend</li>
    <li>No fielding phone calls, no wading through paper registrations. Attendees book on your website, there and then</li>
    <li>No more trips to the bank, take immediate and secure payments online</li>
    <li>Automated confirmation emails so reducing the time need communicating with candidates</li>
    <li>Boost course bookings and reduce administrative time and costs</li>
    <li>Course Admin is Web based meaning you can access your course information from anywhere at any time.</li>
    <li>System is very intuitive and easy to use.</li>
    <li>Lighten your workload</li>
    <li>Upload and manage offline bookings through the admin dashboard</li>
    <li>Keep your attendees organized all the way up to the course date and beyond</li>
  </ul>
</section>

<a class="abs btn btn-large" href="#">
  <svg width="62" height="44" viewBox="0 0 46 34"><path d="M4 12q19-12 38 0l-3 7-8-3v-4q-8-3-16 0v4l-8 3Z" fill="#3b3430"/><rect x="12" y="20" width="22" height="12" rx="3" fill="#3b3430"/></svg>
  <span><span class="main">Contact Us Now</span><br><span class="sub">For a free no obligation discussion about your requiroment and quote.</span></span>
</a>

<footer class="abs footer">| ©2010 Brightmill Works, All Rights Reserved | Disclaimer |</footer>

</body>
</html>
```